Sol Gorditas Digital Menu Boards

IF SELECTED, WINNER MAY BE HIRED FOR OTHER DESIGNS OF DIFFERENT STORES OF OUR COMPANY.

Task: Digital Menu Boards Design

Task description: We need designs for a Digital Menu to be displayed on two 42’’screens at Solgorditas, a fast-food restaurant in Guadalajara, Mexico. The menu redesign should communicate to our customers the experience of eating at our restaurant.

For avoiding the creation of videos, we are expecting several menu slides with the same text but with different images, simulating the effect of a video where the images are changing. This menu slides will be projected through a USB memory and a slideshow.

Attached files:
For the design, there are several documents attached to the task description:
1. Logo of the restaurant
2. Pictures of the restaurant
3. Example video of what we want to achieve through this menu slides.
4. Pictures of the actual menu board, to be replaced with the new designs.
5. Menu description (regular and breakfast menu)
6. Pictures of each element on the menu (We don’t have yet any breakfast pictures)
**The files are organized on a ZIP file.

Expected product:
For the regular menu,
• 2 menu slide designs for TACOS Y ESPECIALIDADES, where the text will be exactly the same but the images would differ.
• 2 menu slide designs for BEBIDAS Y EXTRAS, where the text will be exactly the same but the images would differ.
For the breakfast menu,
• 1 menu slide including all the menu
Total: 5 menu board slides.

Technical specs:
• You should send the editable file, med and high resolution JPGs for each design.
• The designs should fit perfectly on 42’’ screens.

```html
<!DOCTYPE html>
<html lang="es">
<head>
<meta charset="utf-8">
<title>Sol Gorditas — Bebidas y Extras</title>
<link rel="stylesheet" href="https://fonts.googleapis.com/css2?family=Anton&family=Oswald:wght@400;600;700&display=swap">
<style>
  :root {
    --salmon: #f4846c;
    --purple: #5b1d70;
    --ink: #1d1a1a;
    --board-light: #f6f4f2;
    --board-shade: #e4e1de;
    --white: #ffffff;
  }
  * { margin: 0; padding: 0; box-sizing: border-box; }
  html, body { width: 1200px; height: 600px; overflow: hidden; background: var(--white); }
  .menu-board {
    position: relative;
    width: 1200px;
    height: 600px;
    overflow: hidden;
    background: linear-gradient(90deg, var(--board-shade) 0%, var(--board-light) 45%, var(--white) 100%);
    font-family: "Oswald", "Arial Narrow", sans-serif;
    color: var(--ink);
  }
  .drinks-photo {
    position: absolute; left: 0; top: 0; width: 396px; height: 600px;
    background:
      radial-gradient(ellipse at 55% 45%, #e8525c 0%, rgba(232,82,92,0.55) 28%, rgba(232,82,92,0) 50%),
      radial-gradient(ellipse at 18% 35%, #f3d27a 0%, rgba(243,210,122,0) 35%),
      radial-gradient(ellipse at 20% 88%, #b8283a 0%, rgba(184,40,58,0) 18%),
      radial-gradient(ellipse at 80% 85%, #7fa14a 0%, rgba(127,161,74,0) 22%),
      linear-gradient(180deg, #f1efec 0%, #f7f4f0 55%, #d9d2ca 100%);
  }
  .brand-badge {
    position: absolute; left: 326px; top: -5px; width: 168px; height: 168px;
    border-radius: 50%; background: var(--salmon);
    border: 6px solid var(--white);
    display: flex; align-items: center; justify-content: center;
  }
  .brand-name {
    font-family: "Oswald", "Arial Narrow", sans-serif;
    font-weight: 700; font-size: 30px; line-height: 1;
    color: var(--white); text-align: center; width: 130px;
  }
  .band-purple { position: absolute; left: 1108px; top: 0; width: 22px; height: 600px; background: var(--purple); }
  .band-salmon { position: absolute; left: 1144px; top: 0; width: 56px; height: 600px; background: var(--salmon); }
  .section-title {
    position: absolute; right: 113px;
    font-family: "Anton", "Impact", sans-serif; font-size: 40px; line-height: 1;
    letter-spacing: 1px; color: var(--ink);
  }
  .title-drinks { top: 36px; }
  .title-extras { top: 362px; }
  .rule { position: absolute; height: 5px; background: var(--salmon); right: 92px; }
  .rule-drinks { top: 90px; left: 490px; }
  .rule-extras { top: 416px; left: 400px; }
  .item {
    position: absolute; transform: translateX(-50%);
    text-align: center; font-weight: 400; line-height: 1.12; white-space: nowrap;
  }
  .item-lg { font-size: 44px; }
  .item-sm { font-size: 38px; line-height: 1.08; }
  .price {
    position: absolute; width: 94px; height: 94px; margin-left: -47px; margin-top: -47px;
    border-radius: 50%; background: var(--purple); border: 5px solid var(--salmon);
    display: flex; align-items: center; justify-content: center;
    font-family: "Oswald", "Arial Narrow", sans-serif; font-weight: 700; font-size: 34px;
    color: var(--white);
  }
</style>
</head>
<body>
<main class="menu-board">
  <div class="drinks-photo" role="img" aria-label="Frozen fruit drinks in glasses with lemon slices, strawberries and leaves"></div>

  <div class="brand-badge"><span class="brand-name">Sol Gorditas</span></div>

  <div class="band-purple"></div>
  <div class="band-salmon"></div>

  <h2 class="section-title title-drinks">BEBIDAS</h2>
  <div class="rule rule-drinks"></div>

  <p class="item item-lg" style="left:544px; top:126px;">Cerveza<br>Nacional:</p>
  <p class="item item-lg" style="left:753px; top:126px;">Cerveza<br>Importada:</p>
  <p class="item item-sm" style="left:993px; top:112px;">Agua<br>embotellada/<br>Refresco:</p>

  <div class="price" style="left:544px; top:300px;">$30</div>
  <div class="price" style="left:753px; top:300px;">$40</div>
  <div class="price" style="left:993px; top:300px;">$16</div>

  <h2 class="section-title title-extras">EXTRAS</h2>
  <div class="rule rule-extras"></div>

  <p class="item item-lg" style="left:610px; top:430px;">Guacamole:</p>
  <p class="item item-lg" style="left:967px; top:430px;">Postre:</p>

  <div class="price" style="left:610px; top:533px;">$20</div>
  <div class="price" style="left:967px; top:533px;">$15</div>
</main>
</body>
</html>
```